Law Offices business card

Hi there, I'll need business card for the Law Offices of Colby Marchetti. The information must convey his strategic approach and quick resolution to complex business litigation needs. Please emphasize Civil Litigation, Corporate Law, Business Governance and Real Estate Law. Colby has over 25 years of experience in these fields.The card should be modern and edgy and the message should be clear. Please consult his current website for ideas.

```html
<!DOCTYPE html>
<html lang="en">
<head>
<meta charset="utf-8">
<title>Law Offices of Colby Marchetti — Business Card</title>
<link rel="stylesheet" href="https://fonts.googleapis.com/css2?family=Old+Standard+TT:wght@700&family=Open+Sans:wght@400;700&display=swap">
<style>
  :root {
    --stage: #3a3a3c;
    --ink: #0b0b0b;
    --paper: #ffffff;
    --lavender: #aba9c2;
    --red: #dc2a27;
    --soft-white: #d9d8e2;
    --card-w: 620px;
    --card-h: 354px;
  }
  * { margin: 0; padding: 0; box-sizing: border-box; }
  html, body { width: 1200px; height: 900px; overflow: hidden; }
  body {
    background: var(--stage);
    font-family: "Open Sans", Arial, sans-serif;
    position: relative;
  }
  .card {
    position: absolute;
    width: var(--card-w);
    height: var(--card-h);
    border-radius: 22px;
    overflow: hidden;
    box-shadow: 0 14px 30px rgba(0,0,0,.45);
  }
  .card--front { left: 170px; top: 70px; background: var(--ink); }
  .card--back { left: 400px; top: 470px; background: var(--paper); }

  .stripe { position: absolute; left: 0; right: 0; height: 10px; background: var(--lavender); }
  .band { position: absolute; left: 0; right: 0; bottom: 0; }

  .card--front .stripe { top: 214px; }
  .card--front .band { top: 224px; background: var(--red); }
  .card--back .stripe { top: 224px; }
  .card--back .band { top: 234px; background: var(--ink); }

  .firm-name {
    position: absolute;
    left: 0; right: 0;
    font-family: "Old Standard TT", Georgia, serif;
    font-weight: 700;
    text-align: center;
    line-height: 1.05;
  }
  .firm-name__small { display: block; font-size: 20px; letter-spacing: 1px; text-transform: uppercase; }
  .firm-name__large { display: block; font-size: 46px; }
  .card--front .firm-name { top: 58px; color: var(--soft-white); }
  .card--back .firm-name { top: 66px; color: var(--ink); }

  .services {
    position: absolute;
    left: 0; right: 0; top: 16px;
    text-align: center;
    color: var(--paper);
    font-size: 13px;
    line-height: 1.45;
    text-transform: uppercase;
    letter-spacing: .3px;
    list-style: none;
  }
  .services__experience { margin-top: 4px; font-weight: 700; }

  .person {
    position: absolute;
    right: 330px; top: 20px;
    text-align: right;
  }
  .person__name { color: var(--lavender); font-weight: 700; font-size: 22px; letter-spacing: .3px; }
  .person__role { color: var(--red); font-size: 12px; text-transform: uppercase; margin-top: -2px; }
  .person__address { color: var(--soft-white); font-size: 14px; line-height: 1.3; margin-top: 8px; }

  .divider { position: absolute; left: 308px; top: 22px; width: 1px; height: 82px; background: var(--lavender); }

  .contacts {
    position: absolute; left: 322px; top: 20px;
    list-style: none;
    color: var(--soft-white);
    font-size: 14px;
    line-height: 21px;
  }
  .contacts li { display: flex; align-items: center; gap: 8px; }
  .contacts svg { width: 12px; height: 12px; fill: none; stroke: var(--red); stroke-width: 2; flex: none; }
  .contacts svg .solid { fill: var(--red); stroke: none; }
</style>
</head>
<body>

  <section class="card card--front" aria-label="Card front">
    <div class="firm-name">
      <span class="firm-name__small">Law Offices of</span>
      <span class="firm-name__large">Colby Marchetti, PA</span>
    </div>
    <div class="stripe"></div>
    <div class="band">
      <ul class="services">
        <li>Civil Litigation</li>
        <li>Corporate Law</li>
        <li>Business Governance</li>
        <li>Real Estate Law</li>
        <li class="services__experience">Over 25 Years of Experience</li>
      </ul>
    </div>
  </section>

  <section class="card card--back" aria-label="Card back">
    <div class="firm-name">
      <span class="firm-name__small">Law Offices of</span>
      <span class="firm-name__large">Colby Marchetti, PA</span>
    </div>
    <div class="stripe"></div>
    <div class="band">
      <div class="person">
        <p class="person__name">COLBY MARCHETTI</p>
        <p class="person__role">Attorney</p>
        <p class="person__address">118B Harbor Lane<br>Coral Point, FL 33010</p>
      </div>
      <div class="divider"></div>
      <ul class="contacts">
        <li>
          <svg viewBox="0 0 12 12" aria-hidden="true"><path class="solid" d="M2.5 0.5 4.5 2.8 3.4 4.2C4 5.7 6.2 7.9 7.8 8.6L9.2 7.5 11.5 9.5 10.2 11.3C5.5 11 1 6.5 0.7 1.8Z"/></svg>
          555-214-0387
        </li>
        <li>
          <svg viewBox="0 0 12 12" aria-hidden="true"><rect x="3" y="0.8" width="6" height="10.4" rx="1.2"/><circle class="solid" cx="6" cy="9" r="0.8"/></svg>
          555-302-6618
        </li>
        <li>
          <svg viewBox="0 0 12 12" aria-hidden="true"><rect x="0.8" y="2.2" width="10.4" height="7.6" rx="1"/><path d="M1 2.6 6 6.6 11 2.6"/></svg>
          colby@marchettilegal.com
        </li>
        <li>
          <svg viewBox="0 0 12 12" aria-hidden="true"><circle cx="6" cy="6" r="5"/><ellipse cx="6" cy="6" rx="2.2" ry="5"/><path d="M1 6H11"/></svg>
          www.marchettilegal.com
        </li>
      </ul>
    </div>
  </section>

</body>
</html>
```